Fahrzeugbeschriftung für einen Hofladen
Zielgruppe
Biologische Produkte an den Endverbraucher vermarkten. Vorallem Kartoffel, Eier und Getreide.
24 h Hofladen
Aufgabenstellung
ansprechendes Design mit unseren Logo
Es soll das vorhandene Logo + Telfonnummer,Ort und Homepage oben stehn.
KL Lastwiesel R8 Kastenwagen (In Fahrtrichtung links Befindet sich auf der Seite ein Lufthutze)

```html
<!DOCTYPE html>
<html lang="de">
<head>
<meta charset="utf-8">
<title>Hofgut Linde – Fahrzeugbeschriftung</title>
<link rel="stylesheet" href="https://fonts.googleapis.com/css2?family=Open+Sans:wght@400;600;700&display=swap">
<style>
  :root {
    --green: #a9b93c;
    --brown: #6b605c;
    --white: #ffffff;
    --panel: #f4f4f2;
    --line: #c9c9c6;
    --glass: #d9dbdc;
    --trim: #2b2b2b;
    --bg: #ffffff;
  }
  html, body { margin: 0; padding: 0; overflow: hidden; background: var(--bg); }
  .canvas { width: 1200px; height: 1198px; display: block; }
  .wordmark { font-family: "Open Sans", sans-serif; font-weight: 600; fill: var(--brown); }
  .phone { font-family: "Open Sans", sans-serif; font-weight: 700; }
  .phone--side { fill: var(--green); }
  .phone--rear { fill: var(--brown); }
  .address { font-family: "Open Sans", sans-serif; font-weight: 400; fill: var(--brown); }
  .web { font-family: "Open Sans", sans-serif; font-weight: 400; fill: var(--white); }
  .body-shell { fill: var(--white); stroke: var(--line); stroke-width: 3; }
  .glass { fill: var(--glass); }
  .band-green { fill: var(--green); }
  .band-brown { fill: var(--brown); }
  .trim { fill: var(--trim); }
  .logo-field { fill: var(--panel); }
  .logo-dot { fill: var(--green); }
</style>
</head>
<body>
<svg class="canvas" viewBox="0 0 1504 1502" xmlns="http://www.w3.org/2000/svg" aria-label="Fahrzeugbeschriftung Hofgut Linde, Seiten- und Heckansicht">
  <defs>
    <clipPath id="side-clip">
      <path d="M50,525 L55,330 Q80,300 250,232 L470,80 Q500,50 560,45 L1360,42 Q1390,45 1400,110 L1440,470 L1440,525 Z"/>
    </clipPath>
    <clipPath id="rear-clip">
      <path d="M445,1360 L450,960 Q470,780 520,700 Q540,685 600,684 L1110,684 Q1170,685 1190,705 Q1235,790 1248,960 L1250,1360 Z"/>
    </clipPath>
  </defs>

  <!-- Seitenansicht -->
  <g class="side-view">
    <path class="body-shell" d="M50,525 L55,330 Q80,300 250,232 L470,80 Q500,50 560,45 L1360,42 Q1390,45 1400,110 L1440,470 L1440,525 Z"/>
    <path class="glass" d="M400,235 L480,85 L665,78 L660,240 Z"/>
    <g clip-path="url(#side-clip)">
      <path class="band-green" d="M405,465 C650,400 1000,320 1440,318 L1440,405 C1400,385 1300,366 1150,366 C900,366 650,410 420,460 Z"/>
      <path class="band-brown" d="M425,470 C650,424 900,380 1150,378 C1300,378 1400,398 1440,418 L1440,475 L425,475 Z"/>
      <path class="trim" d="M418,522 L438,487 L452,487 L432,522 Z M446,522 L466,487 L480,487 L460,522 Z M474,522 L494,487 L508,487 L488,522 Z M502,522 L522,487 L1050,487 L1050,522 Z"/>
    </g>
    <text class="web" x="880" y="442" text-anchor="middle" font-size="30">www.hofgutlinde.at</text>

    <rect class="logo-field" x="705" y="70" width="340" height="168"/>
    <circle class="logo-dot" cx="748" cy="154" r="26"/>
    <text class="wordmark" x="786" y="136" font-size="40">Hofgut</text>
    <text class="wordmark" x="786" y="190" font-size="40">Linde</text>

    <text class="phone phone--side" x="1192" y="133" text-anchor="middle" font-size="32">02731/58264</text>
    <text class="address" x="1133" y="163" font-size="17">Hofgut Linde</text>
    <text class="address" x="1133" y="185" font-size="17">Mühlweg 7</text>
    <text class="address" x="1133" y="207" font-size="17">4812 Kornau</text>
  </g>

  <!-- Heckansicht -->
  <g class="rear-view">
    <path class="body-shell" d="M445,1360 L450,960 Q470,780 520,700 Q540,685 600,684 L1110,684 Q1170,685 1190,705 Q1235,790 1248,960 L1250,1360 Z"/>
    <g clip-path="url(#rear-clip)">
      <path class="band-green" d="M440,1150 Q845,1270 1260,1150 L1260,1268 Q845,1215 440,1268 Z"/>
      <path class="band-brown" d="M440,1282 Q845,1228 1260,1282 L1260,1360 L440,1360 Z"/>
    </g>
    <rect class="trim" x="440" y="1355" width="812" height="48" rx="8"/>
    <rect class="trim" x="525" y="1082" width="308" height="30" rx="6"/>

    <circle class="logo-dot" cx="690" cy="850" r="40"/>
    <text class="wordmark" x="750" y="820" font-size="64">Hofgut</text>
    <text class="wordmark" x="750" y="900" font-size="64">Linde</text>

    <text class="phone phone--rear" x="698" y="1050" text-anchor="middle" font-size="38">02731/58264</text>
    <text class="address" x="887" y="1019" font-size="18">Hofgut Linde</text>
    <text class="address" x="887" y="1043" font-size="18">Mühlweg 7</text>
    <text class="address" x="887" y="1067" font-size="18">4812 Kornau</text>

    <text class="web" x="845" y="1310" text-anchor="middle" font-size="36">www.hofgutlinde.at</text>
  </g>
</svg>
</body>
</html>
```